Vell Studio - Lash Serum Packaging

Need Packaging done for this Lash Serum for a brand called "Vell Studio". The bottle will remain black but the box can be any color. This will be for a 3ml bottle. Give me different options for packaging that is minimalist and clean for this brand that makes it look expensive and make people want to buy.

```html
<!DOCTYPE html>
<html lang="en">
<head>
<meta charset="utf-8">
<title>Vell Studio – Lash &amp; Brow Serum Packaging</title>
<link href="https://fonts.googleapis.com/css2?family=Arimo:wght@700&family=Montserrat:wght@600&display=swap" rel="stylesheet">
<style>
  :root {
    --cream: #f5f1e3;
    --sand: #e4d6c2;
    --ink: #201f20;
    --gold: #d2ae6b;
  }
  html, body {
    margin: 0;
    padding: 0;
    overflow: hidden;
  }
  body {
    width: 868px;
    height: 1200px;
    background: linear-gradient(to bottom, var(--cream) 0%, var(--cream) 56%, var(--sand) 76%, var(--sand) 100%);
  }
  .packaging {
    display: block;
    width: 868px;
    height: 1200px;
  }
  .panel { fill: var(--ink); }
  .glow-stop-core { stop-color: var(--gold); stop-opacity: 0.85; }
  .glow-stop-mid { stop-color: var(--gold); stop-opacity: 0.3; }
  .glow-stop-edge { stop-color: var(--gold); stop-opacity: 0; }
  .brand-name {
    font-family: "Montserrat", sans-serif;
    font-weight: 600;
    fill: var(--gold);
    letter-spacing: 1px;
  }
  .product-name {
    font-family: "Arimo", sans-serif;
    font-weight: 700;
    fill: var(--gold);
  }
  .volume-pill { fill: var(--gold); }
  .volume-text {
    font-family: "Arimo", sans-serif;
    font-weight: 700;
    fill: var(--ink);
    font-size: 19px;
  }
</style>
</head>
<body>
<svg class="packaging" viewBox="0 0 868 1200" xmlns="http://www.w3.org/2000/svg">
  <defs>
    <radialGradient id="box-glow" cx="0.5" cy="0.5" r="0.5">
      <stop class="glow-stop-core" offset="0"/>
      <stop class="glow-stop-mid" offset="0.55"/>
      <stop class="glow-stop-edge" offset="1"/>
    </radialGradient>
    <radialGradient id="bottle-glow" cx="0.2" cy="0.55" r="0.6">
      <stop class="glow-stop-core" offset="0"/>
      <stop class="glow-stop-mid" offset="0.5"/>
      <stop class="glow-stop-edge" offset="1"/>
    </radialGradient>
    <clipPath id="bottle-body-clip"><path d="M535 512 Q607 504 680 509 L680 1070 Q680 1081 668 1081 L547 1081 Q535 1081 535 1070 Z"/></clipPath>
  </defs>

  <!-- Box -->
  <g class="box">
    <rect class="panel" x="183" y="108" width="259" height="988"/>
    <text class="brand-name" x="312" y="242" font-size="27" text-anchor="middle" dominant-baseline="central">VELL STUDIO</text>
    <text class="product-name" font-size="50" text-anchor="middle" dominant-baseline="central" transform="translate(355 541) rotate(90)">LASH &amp; BROW</text>
    <text class="product-name" font-size="50" text-anchor="middle" dominant-baseline="central" transform="translate(297 541) rotate(90)">SERUM</text>
    <rect class="box-accent" role="img" aria-label="Soft gold bubble decoration" x="190" y="770" width="245" height="250" fill="url(#box-glow)"/>
    <rect class="volume-pill" x="277" y="1033" width="71" height="26" rx="8"/>
    <text class="volume-text" x="312.5" y="1047" text-anchor="middle" dominant-baseline="central">3ml</text>
  </g>

  <!-- Bottle -->
  <g class="bottle">
    <path class="panel bottle-cap" d="M535 162 Q535 154 548 153 Q607 149 668 152 Q678 154 678 164 L680 505 Q607 499 536 505 Z"/>
    <path class="panel bottle-body" d="M535 512 Q607 504 680 509 L680 1070 Q680 1081 668 1081 L547 1081 Q535 1081 535 1070 Z"/>
    <text class="brand-name" font-size="25" text-anchor="middle" dominant-baseline="central" transform="translate(607 664) rotate(90)">VELL STUDIO</text>
    <text class="product-name" font-size="27" text-anchor="middle" dominant-baseline="central" transform="translate(647 899) rotate(90)">LASH &amp; BROW</text>
    <text class="product-name" font-size="27" text-anchor="middle" dominant-baseline="central" transform="translate(619 899) rotate(90)">SERUM</text>
    <g clip-path="url(#bottle-body-clip)">
      <rect class="bottle-accent" role="img" aria-label="Soft gold bubble decoration" x="535" y="870" width="70" height="211" fill="url(#bottle-glow)"/>
    </g>
    <rect class="volume-pill" x="573" y="1035" width="70" height="24" rx="8"/>
    <text class="volume-text" x="608" y="1048" text-anchor="middle" dominant-baseline="central">3ml</text>
  </g>
</svg>
</body>
</html>
```